Lumen Bridge Collective Slide Deck Template

Design a slide deck template to be used for pitch deck for a company who will be offering services to connect rare disease patients to other patients, pharma/biotech industry in partnership to raise awareness of rare disease, living with a rare disease and treatment choices through on line and in person programs. We need a human element, one that inspires trust and confidence that can be used as a template for our pitch deck etc. We have a logo in progress which will need to have a placeholder for on the slide deck. Thank you

Target Market(s)

Pharma/biotech sector and rare disease patients

Industry/Entity Type

Biotechnology

Font styles to use
Serif
Sans Serif

Colors
63c5b5
00a990
86cfc6
cfeae6
edf8f6
85cae6
0293ce
33a6d7
cee9f5

Requirements
Must have
• Human element. Rare disease aspect if possible. Must inspire trust and confidence.
Nice to have
• Space for our logo which is in development

```html
<!DOCTYPE html>
<html lang="en">
<head>
<meta charset="utf-8">
<title>Lumen Bridge Collective – Slide Deck Template</title>
<link href="https://fonts.googleapis.com/css2?family=Raleway:wght@300;400;600;700&family=Lora:wght@400;600&display=swap" rel="stylesheet">
<style>
:root{
  --teal:#00a990;
  --teal-mid:#63c5b5;
  --teal-soft:#86cfc6;
  --teal-pale:#cfeae6;
  --teal-mist:#edf8f6;
  --blue-soft:#85cae6;
  --blue:#0293ce;
  --blue-mid:#33a6d7;
  --blue-pale:#cee9f5;
  --ink:#555;
  --muted:#a4a4a4;
  --grey:#6d6d6d;
  --page:#e9ecee;
}
*{box-sizing:border-box;margin:0;padding:0}
html,body{width:900px;height:1200px;overflow:hidden;background:var(--page)}
body{font-family:"Raleway",sans-serif;color:var(--ink)}
.deck{display:grid;grid-template-columns:repeat(6,145px);column-gap:6px;grid-auto-rows:166px;row-gap:5px;padding-top:4px;width:900px;height:1200px}
.slide{grid-column:span 2;position:relative;background:#fff;overflow:hidden;box-shadow:0 1px 3px rgba(0,0,0,.18)}
.deck .last-a{grid-column:2/span 2}
.deck .last-b{grid-column:4/span 2}
.title{position:absolute;left:13px;top:11px;font-size:10.5px;font-weight:400;color:var(--blue)}
.title::after{content:"";display:block;width:18px;height:1px;background:var(--teal-soft);margin-top:4px}
.logo{position:absolute;right:8px;top:12px;display:flex;align-items:center;gap:3px;font-size:5.5px;font-weight:400;color:var(--blue-mid)}
.logo i{width:5px;height:5px;border-radius:50%;background:var(--teal)}
.foot{position:absolute;left:0;right:0;bottom:0;height:7px;background:var(--teal);font-size:2.8px;color:#dff;padding:2px 0 0 14px}
.foot::after{content:"";position:absolute;right:0;top:0;width:7px;height:7px;background:var(--blue)}
.photo{position:absolute;background:linear-gradient(135deg,#d6dde3,#9fb2c0 55%,#6f8796)}
.photo.warm{background:linear-gradient(135deg,#e9e1d8,#b9c4cc 50%,#7d94a3)}
.photo.cool{background:linear-gradient(135deg,#cbe4ee,#8fb8cd 55%,#4e7f99)}
.tx{font-size:3.6px;line-height:1.4;color:var(--muted)}
.abs{position:absolute}
.h6{font-size:5.5px;color:var(--blue);font-weight:400}
.white{color:#fff}
.ico{position:absolute;width:9px;height:9px;border-radius:50%;background:var(--blue)}
.ico.t{background:var(--teal)}.ico.l{background:var(--blue-soft)}.ico.g{background:var(--teal-soft)}
/* team */
.member{position:absolute;width:120px}
.member .av{position:absolute;left:0;top:0;width:20px;height:20px;border-radius:50%;background:linear-gradient(135deg,#d9d2cc,#8a9aa5)}
.member .nm{position:absolute;left:28px;top:0;font-size:5px;color:var(--blue)}
.member .tx{position:absolute;left:28px;top:7px;width:92px}
/* timeline */
.vline{position:absolute;width:1px;background:var(--teal-pale)}
.dot{position:absolute;width:5px;height:5px;border-radius:50%;background:var(--blue)}
.pct{font-family:"Lora",serif;font-weight:600}
</style>
</head>
<body>
<main class="deck">

<!-- 1 Our Team -->
<section class="slide">
  <h2 class="title">Our Team</h2>
  <div class="logo"><i></i>Lumen Bridge Collective</div>
  <div class="member" style="left:14px;top:36px"><div class="av" role="img" aria-label="Portrait of team member"></div><div class="nm">Michael Doe</div><p class="tx">CEO, MBA and CMA<br>• Guides patient partnerships and sets the group vision.<br>• Leads pharma outreach work.</p></div>
  <div class="member" style="left:154px;top:36px"><div class="av" role="img" aria-label="Portrait of team member"></div><div class="nm">James Doe</div><p class="tx">Manager, M.B.A<br>• Runs online and in person programs.<br>• Builds trust with families.</p></div>
  <div class="member" style="left:14px;top:92px"><div class="av" role="img" aria-label="Portrait of team member"></div><div class="nm">Jane Doe</div><p class="tx">Doctor of Chemistry, M.B.A<br>• Shapes treatment choice guides for patients.<br>• Reviews research updates.</p></div>
  <div class="member" style="left:154px;top:92px"><div class="av" role="img" aria-label="Portrait of team member"></div><div class="nm">John Doe</div><p class="tx">Doctor of Physics, Professor<br>• Advises on rare disease science.<br>• Hosts awareness events.</p></div>
  <div class="foot">© Copyright 2018 Lumen Bridge Collective. All rights reserved.</div>
</section>

<!-- 2 Testimonials -->
<section class="slide">
  <h2 class="title">Customer Testimonials</h2>
  <div class="logo"><i></i>Lumen Bridge Collective</div>
  <div class="abs" role="img" aria-label="Portrait of patient" style="left:64px;top:34px;width:38px;height:38px;border-radius:50%;background:linear-gradient(135deg,#d8d2cc,#7d8c97)"></div>
  <p class="tx abs" style="left:128px;top:46px;width:140px">This network helped our family find other patients and clear answers about treatment choices we never knew we had.</p>
  <div class="abs" style="left:0;right:0;top:88px;bottom:0;background:var(--teal)">
    <svg class="abs" width="296" height="78" style="left:0;top:0">
      <g fill="none" stroke="#fff" stroke-width=".8">
        <circle cx="70" cy="24" r="10"/><circle cx="126" cy="24" r="10"/><circle cx="182" cy="24" r="10"/><circle cx="238" cy="24" r="10"/>
        <rect x="66" y="20" width="8" height="8"/><rect x="122" y="20" width="8" height="8"/><rect x="178" y="20" width="8" height="8"/><rect x="234" y="20" width="8" height="8"/>
      </g>
    </svg>
    <p class="tx abs white" style="left:52px;top:40px;width:36px;text-align:center">Why does finding help take so long for families?</p>
    <p class="tx abs white" style="left:108px;top:40px;width:36px;text-align:center">Who do I ask about trial options near me?</p>
    <p class="tx abs white" style="left:164px;top:40px;width:36px;text-align:center">How can patients meet others living the same way?</p>
    <p class="tx abs white" style="left:220px;top:40px;width:36px;text-align:center">Where can industry hear the patient voice?</p>
  </div>
  <div class="foot">© Copyright 2018 Lumen Bridge Collective. All rights reserved.</div>
</section>

<!-- 3 Two Pictures -->
<section class="slide">
  <h2 class="title">Two Pictures Slide</h2>
  <div class="logo"><i></i>Lumen Bridge Collective</div>
  <div class="photo cool" role="img" aria-label="Photo of doctors reviewing a case together" style="left:22px;top:33px;width:124px;height:114px"></div>
  <div class="photo" role="img" aria-label="Photo of clinicians discussing treatment" style="left:150px;top:33px;width:124px;height:114px"></div>
  <div class="foot">© Copyright 2018 Lumen Bridge Collective. All rights reserved.</div>
</section>

<!-- 4 Title and Image + Text -->
<section class="slide">
  <h2 class="title">Title And Image + Text</h2>
  <div class="logo"><i></i>Lumen Bridge Collective</div>
  <div class="photo warm" role="img" aria-label="Photo of a doctor speaking with a patient" style="left:22px;top:33px;width:256px;height:62px"></div>
  <p class="abs" style="left:22px;top:100px;width:120px;font-size:5px;line-height:1.35;color:var(--blue-mid)">Connecting people living with rare disease to peers, care teams and industry partners through trusted programs.</p>
  <p class="tx abs" style="left:150px;top:100px;width:126px">Our online and in person sessions help patients share stories, learn about treatment choices and build awareness. Partners gain real insight from the community while patients gain support, answers and a louder voice in research.</p>
  <div class="foot">© Copyright 2018 Lumen Bridge Collective. All rights reserved.</div>
</section>

<!-- 5 Sales Comparison -->
<section class="slide">
  <h2 class="title">Sales Comparison</h2>
  <div class="logo"><i></i>Lumen Bridge Collective</div>
  <svg class="abs" width="296" height="120" style="left:0;top:40px">
    <g font-family="Raleway" font-size="4" fill="#888"><text x="50" y="11">2018 Sales</text><text x="218" y="11">2019 Sales</text></g>
    <g fill="var(--blue)"><rect x="21" y="28" width="8" height="36"/><rect x="44" y="44" width="8" height="20"/><rect x="67" y="39" width="8" height="25"/><rect x="90" y="26" width="8" height="38"/></g>
    <g fill="var(--teal)"><rect x="195" y="28" width="8" height="36"/><rect x="218" y="44" width="8" height="20"/><rect x="241" y="38" width="8" height="26"/><rect x="264" y="26" width="8" height="38"/></g>
    <line x1="146" y1="15" x2="146" y2="118" stroke="#ccc" stroke-dasharray="2 2" stroke-width=".6"/>
    <ellipse cx="146" cy="44" rx="14" ry="9" fill="var(--blue-soft)"/><text x="141" y="46" font-size="5" fill="#fff" font-family="Raleway">VS</text>
    <line x1="18" y1="64" x2="100" y2="64" stroke="#ddd" stroke-width=".5"/><line x1="192" y1="64" x2="274" y2="64" stroke="#ddd" stroke-width=".5"/>
  </svg>
  <div class="abs pct" style="left:22px;top:126px;font-size:13px;color:var(--blue)">45%</div>
  <p class="tx abs" style="left:57px;top:126px;width:50px"><span style="color:var(--blue)">Programs grown</span><br>new members joined</p>
  <div class="abs pct" style="left:190px;top:126px;font-size:13px;color:var(--teal)">68%</div>
  <p class="tx abs" style="left:226px;top:126px;width:50px"><span style="color:var(--teal)">Programs grown</span><br>new members joined</p>
  <div class="foot">© Copyright 2018 Lumen Bridge Collective. All rights reserved.</div>
</section>

<!-- 6 Your Title Goes Here -->
<section class="slide">
  <div class="photo" role="img" aria-label="Soft grey photo of a care team" style="left:0;top:0;width:296px;height:74px;background:linear-gradient(135deg,#cfd3d6,#b4b9bd)"></div>
  <div class="abs white" style="left:100px;top:24px;font-size:9px;font-weight:300">Your Title Goes Here</div>
  <div class="abs" style="left:0;top:74px;width:99px;bottom:0;background:var(--blue-mid)"><p class="tx white" style="padding:10px 8px">Patients meet peers who share the same rare condition. Guided sessions build knowledge and ease the feeling of facing it alone, with care teams close by.</p></div>
  <div class="abs" style="left:99px;top:74px;width:98px;bottom:0;background:var(--teal)"><p class="tx white" style="padding:10px 8px">Industry partners hear real patient needs. Joint programs raise awareness and shape studies around daily life with a rare disease.</p></div>
  <div class="abs" style="left:197px;top:74px;width:99px;bottom:0;background:#6a6a6a"><p class="tx white" style="padding:10px 8px">Clear guides on treatment choices help families speak with doctors and make informed decisions together.</p></div>
</section>

<!-- 7 Timeline title -->
<section class="slide">
  <div class="abs" style="left:0;top:0;width:296px;height:72px;background:var(--teal)"></div>
  <div class="abs white" style="left:0;width:296px;top:22px;text-align:center;font-size:10px;font-weight:300">Lumen Bridge Collective</div>
  <div class="abs white" style="left:0;width:296px;top:50px;text-align:center;font-size:8px">This Is Your Timeline Page</div>
  <div class="abs" style="left:0;width:296px;top:79px;text-align:center;font-size:5px;color:var(--blue)">Your Heading Here</div>
  <p class="tx abs" style="left:100px;top:86px;width:96px;text-align:center">From our first patient meeting to national programs, each step brought more people together around rare disease.</p>
  <div class="vline" style="left:147px;top:112px;height:54px"></div>
  <div class="dot" style="left:145px;top:140px"></div>
</section>

<!-- 8 Your Title photo right -->
<section class="slide">
  <h2 class="title">Your Title</h2>
  <div class="photo warm" role="img" aria-label="Photo of a smiling medical team" style="left:148px;top:0;width:148px;height:83px"></div>
  <div class="abs" style="left:21px;top:43px;width:6px;height:6px;border:1px solid var(--blue-soft);transform:rotate(45deg)"></div>
  <div class="h6 abs" style="left:32px;top:43px">Bullet Point</div>
  <p class="tx abs" style="left:32px;top:50px;width:100px">Patient circles meet each month online and in person to share what works.</p>
  <div class="abs" style="left:0;top:83px;width:148px;bottom:0;background:var(--teal)"><p class="tx white" style="padding:10px 10px">We bring patients, families and the pharma and biotech sector together to raise awareness of rare disease and of what living with it truly means.<br><br>Each program is built with patients, for patients, so every voice is heard.</p></div>
  <svg class="abs" width="8" height="8" style="left:156px;top:110px"><rect x="0" y="3" width="1.5" height="5" fill="var(--teal-soft)"/><rect x="3" y="1" width="1.5" height="7" fill="var(--teal-soft)"/><rect x="6" y="4" width="1.5" height="4" fill="var(--teal-soft)"/></svg>
  <div class="h6 abs" style="left:169px;top:110px;color:var(--teal-soft)">Bullet Point</div>
  <p class="tx abs" style="left:169px;top:117px;width:100px">Partners join to learn from lived experience and shape better care.</p>
</section>

<!-- 9 Your Title photo right, blue -->
<section class="slide">
  <h2 class="title">Your Title</h2>
  <div class="photo" role="img" aria-label="Photo of a senior doctor holding a folder" style="left:148px;top:0;width:148px;height:83px;background:linear-gradient(135deg,#f2f4f6,#c9d3da)"></div>
  <div class="abs" style="left:21px;top:43px;width:6px;height:6px;border:1px solid var(--blue-soft);transform:rotate(45deg)"></div>
  <div class="h6 abs" style="left:32px;top:43px">Bullet Point</div>
  <p class="tx abs" style="left:32px;top:50px;width:100px">Trusted guidance on diagnosis, support and care options.</p>
  <svg class="abs" width="8" height="8" style="left:20px;top:82px"><rect x="0" y="3" width="1.5" height="5" fill="var(--blue-soft)"/><rect x="3" y="1" width="1.5" height="7" fill="var(--blue-soft)"/><rect x="6" y="4" width="1.5" height="4" fill="var(--blue-soft)"/></svg>
  <div class="h6 abs" style="left:32px;top:82px">Chart</div>
  <p class="tx abs" style="left:32px;top:89px;width:100px">Program reach and member growth shown in one simple view.</p>
  <svg class="abs" width="8" height="8" style="left:20px;top:116px"><g fill="var(--blue-soft)"><circle cx="1.5" cy="4" r="1.4"/><circle cx="6.5" cy="1.5" r="1.4"/><circle cx="6.5" cy="6.5" r="1.4"/></g><path d="M1.5 4L6.5 1.5M1.5 4L6.5 6.5" stroke="var(--blue-soft)" stroke-width=".6"/></svg>
  <div class="h6 abs" style="left:32px;top:116px">Share</div>
  <p class="tx abs" style="left:32px;top:123px;width:100px">Stories shared across the community inspire hope and trust.</p>
  <div class="abs" style="left:148px;top:83px;width:148px;bottom:0;background:var(--blue)"><p class="tx white" style="padding:14px 10px">Our mission is to connect people living with rare disease to each other and to the partners who can help them thrive.<br><br>Together we turn awareness into action and real change.</p></div>
</section>

<!-- 10 Timeline middle -->
<section class="slide">
  <div class="vline" style="left:147px;top:0;height:166px"></div>
  <div class="dot" style="left:145px;top:18px"></div><div class="dot" style="left:145px;top:47px"></div><div class="dot" style="left:145px;top:108px"></div>
  <div class="abs" style="left:108px;top:18px;font-size:4px;color:var(--blue)">Your Title</div>
  <p class="tx abs" style="left:40px;top:25px;width:100px;text-align:right">First patient circle meets and shares stories.</p>
  <div class="abs" style="left:160px;top:53px;font-size:4px;color:var(--blue)">Your Title</div>
  <div class="abs pct" style="left:160px;top:58px;font-size:11px;color:#444">85%</div>
  <p class="tx abs" style="left:160px;top:73px;width:84px">Members say they feel less alone after joining.</p>
  <div class="abs" style="left:108px;top:108px;font-size:4px;color:var(--blue)">Your Title</div>
  <div class="abs" style="left:56px;top:117px;width:78px;height:30px;background:var(--teal)"><p class="tx white" style="padding:5px;text-align:center">First pharma partner joins the awareness program.</p></div>
</section>

<!-- 11 Who We Are -->
<section class="slide">
  <h2 class="title">Who We Are?</h2>
  <div class="logo"><i></i>Lumen Bridge Collective</div>
  <div class="abs" style="left:22px;top:37px;font-size:7px;line-height:1.15;color:var(--teal-mid)">A Title About<br>Contents<br><span class="tx" style="color:var(--teal-mid)">Short caption here</span></div>
  <p class="tx abs" style="left:90px;top:37px;width:190px">2017<br>We began as a small patient group meeting online. Families found each other, swapped advice and asked for a place to grow.</p>
  <div class="abs" style="left:90px;top:55px;width:186px;height:1px;background:var(--blue-soft)"></div>
  <div class="abs" style="left:22px;top:75px;font-size:7px;line-height:1.15;color:var(--teal-mid)">A Title About<br>Contents<br><span class="tx" style="color:var(--teal-mid)">Short caption here</span></div>
  <p class="tx abs" style="left:90px;top:75px;width:190px">2018<br>In person events launched and the first industry partners joined to listen, learn and support awareness.</p>
  <div class="abs" style="left:90px;top:93px;width:186px;height:1px;background:var(--blue-soft)"></div>
  <div class="abs" style="left:22px;top:113px;font-size:7px;line-height:1.15;color:var(--blue-soft)">A Title About<br>Contents<br><span class="tx" style="color:var(--blue-soft)">Short caption here</span></div>
  <p class="tx abs" style="left:90px;top:113px;width:190px">2019<br>Programs now reach patients across regions with guides on living with rare disease and treatment choices.</p>
  <div class="foot">© Copyright 2018 Lumen Bridge Collective. All rights reserved.</div>
</section>

<!-- 12 Bullet & Chart pie -->
<section class="slide">
  <h2 class="title">Bullet &amp; Chart Area</h2>
  <div class="logo"><i></i>Lumen Bridge Collective</div>
  <svg class="abs" width="130" height="110" style="left:20px;top:40px" viewBox="0 0 130 110">
    <g transform="rotate(-90 72 50)" fill="none" stroke-width="36">
      <circle cx="72" cy="50" r="18" stroke="var(--blue-mid)" stroke-dasharray="67.86 113.1"/>
      <circle cx="72" cy="50" r="18" stroke="var(--teal)" stroke-dasharray="28.27 113.1" stroke-dashoffset="-67.86"/>
      <circle cx="72" cy="50" r="18" stroke="var(--blue-soft)" stroke-dasharray="16.96 113.1" stroke-dashoffset="-96.13"/>
      <circle cx="72" cy="50" r="18" stroke="var(--teal-soft)" stroke-dasharray="11.31 113.1" stroke-dashoffset="-113.1"/>
    </g>
    <g font-family="Lora" font-size="7" fill="var(--teal-soft)"><text x="52" y="8">10%</text><text x="9" y="38">15%</text><text x="7" y="81">25%</text><text x="106" y="58" fill="var(--blue)">60%</text></g>
    <g font-size="2.5" fill="#999" font-family="Raleway"><text x="40" y="100">■ 1st Qtr ■ 2nd Qtr ■ 3rd Qtr ■ 4th Qtr</text></g>
  </svg>
  <div class="ico" style="left:190px;top:58px"></div><div class="h6 abs" style="left:204px;top:58px">Category One</div><p class="tx abs" style="left:204px;top:64px;width:72px">Patients in peer circles.</p>
  <div class="ico t" style="left:190px;top:82px"></div><div class="h6 abs" style="left:204px;top:82px;color:var(--teal)">Category Two</div><p class="tx abs" style="left:204px;top:88px;width:72px">Families in online talks.</p>
  <div class="ico l" style="left:190px;top:106px"></div><div class="h6 abs" style="left:204px;top:106px;color:var(--blue-soft)">Category Three</div><p class="tx abs" style="left:204px;top:112px;width:72px">Care teams in events.</p>
  <div class="ico g" style="left:190px;top:130px"></div><div class="h6 abs" style="left:204px;top:130px;color:var(--teal-soft)">Category Four</div><p class="tx abs" style="left:204px;top:136px;width:72px">Industry partners.</p>
  <div class="foot">© Copyright 2018 Lumen Bridge Collective. All rights reserved.</div>
</section>

<!-- 13 Timeline end -->
<section class="slide">
  <div class="vline" style="left:147px;top:0;height:110px"></div>
  <div class="dot" style="left:145px;top:26px"></div><div class="dot" style="left:145px;top:77px"></div><div class="dot" style="left:145px;top:96px"></div>
  <div class="abs" style="left:162px;top:18px;font-size:7px;font-weight:700;line-height:1.2;color:var(--blue)">Your<br>Title Here</div>
  <p class="tx abs" style="left:162px;top:43px;width:100px">Regional programs open with partner support.</p>
  <div class="abs" style="left:96px;top:50px;font-size:5px;line-height:1.1;font-weight:600;text-align:right;color:var(--blue)">Timeline<br>Finish</div>
  <p class="tx abs" style="left:30px;top:63px;width:66px;text-align:right">Half of members now join in person too.</p>
  <div class="abs pct" style="left:104px;top:63px;font-size:11px;color:var(--blue)">50%</div>
  <div class="abs" style="left:162px;top:96px;font-size:4px;color:var(--blue)">Your Title</div>
  <p class="tx abs" style="left:162px;top:101px;width:100px">New treatment choice guides launch for all.</p>
  <div class="abs" style="left:0;width:296px;top:138px;text-align:center;font-size:10px;font-weight:300;color:var(--blue-mid)">Lumen Bridge Collective</div>
</section>

<!-- 14 Horizontal bars -->
<section class="slide">
  <h2 class="title">Bullet &amp; Chart Area</h2>
  <div class="logo"><i></i>Lumen Bridge Collective</div>
  <svg class="abs" width="150" height="100" style="left:22px;top:40px">
    <g font-family="Raleway" font-size="2.5" fill="#999"><text x="0" y="14">Category 4</text><text x="0" y="35">Category 3</text><text x="0" y="56">Category 2</text><text x="0" y="77">Category 1</text></g>
    <g><rect x="20" y="8" width="80" height="3" fill="var(--blue)"/><rect x="20" y="12" width="55" height="3" fill="var(--teal)"/><rect x="20" y="16" width="70" height="3" fill="var(--blue-soft)"/>
    <rect x="20" y="29" width="45" height="3" fill="var(--blue)"/><rect x="20" y="33" width="28" height="3" fill="var(--teal)"/><rect x="20" y="37" width="70" height="3" fill="var(--blue-soft)"/>
    <rect x="20" y="50" width="60" height="3" fill="var(--blue)"/><rect x="20" y="54" width="90" height="3" fill="var(--teal)"/><rect x="20" y="58" width="75" height="3" fill="var(--blue-soft)"/>
    <rect x="20" y="71" width="30" height="3" fill="var(--blue)"/><rect x="20" y="75" width="40" height="3" fill="var(--teal)"/><rect x="20" y="79" width="85" height="3" fill="var(--blue-soft)"/></g>
    <text x="40" y="96" font-size="2.5" fill="#999" font-family="Raleway">■ Series 1 ■ Series 2 ■ Series 3</text>
  </svg>
  <div class="ico" style="left:185px;top:50px"></div><div class="h6 abs" style="left:198px;top:50px">Category One</div><p class="tx abs" style="left:198px;top:56px;width:78px">Online peer sessions.</p>
  <div class="ico t" style="left:185px;top:74px"></div><div class="h6 abs" style="left:198px;top:74px;color:var(--teal)">Category Two</div><p class="tx abs" style="left:198px;top:80px;width:78px">In person meetups.</p>
  <div class="ico l" style="left:185px;top:98px"></div><div class="h6 abs" style="left:198px;top:98px;color:var(--blue-soft)">Category Three</div><p class="tx abs" style="left:198px;top:104px;width:78px">Awareness campaigns.</p>
  <div class="ico g" style="left:185px;top:122px"></div><div class="h6 abs" style="left:198px;top:122px;color:var(--teal-soft)">Category Four</div><p class="tx abs" style="left:198px;top:128px;width:78px">Partner workshops.</p>
  <div class="foot">© Copyright 2018 Lumen Bridge Collective. All rights reserved.</div>
</section>

<!-- 15 Vertical bars -->
<section class="slide">
  <h2 class="title">Bullet &amp; Chart Area</h2>
  <div class="logo"><i></i>Lumen Bridge Collective</div>
  <div class="ico" style="left:22px;top:40px"></div><div class="h6 abs" style="left:36px;top:40px">Your Text Here</div><p class="tx abs" style="left:36px;top:46px;width:90px">Members connected this year.</p>
  <div class="ico t" style="left:22px;top:64px"></div><div class="h6 abs" style="left:36px;top:64px">Your Text Here</div><p class="tx abs" style="left:36px;top:70px;width:90px">Programs held in person.</p>
  <div class="ico l" style="left:22px;top:88px"></div><div class="h6 abs" style="left:36px;top:88px;color:var(--blue-soft)">Your Text Here</div><p class="tx abs" style="left:36px;top:94px;width:90px">Partners in awareness work.</p>
  <div class="ico g" style="left:22px;top:112px"></div><div class="h6 abs" style="left:36px;top:112px;color:var(--teal-soft)">Your Text Here</div><p class="tx abs" style="left:36px;top:118px;width:90px">Guides shared with families.</p>
  <svg class="abs" width="130" height="100" style="left:150px;top:40px">
    <g><rect x="8" y="20" width="4" height="50" fill="var(--blue)"/><rect x="12" y="42" width="4" height="28" fill="var(--teal)"/><rect x="16" y="35" width="4" height="35" fill="var(--blue-soft)"/>
    <rect x="36" y="38" width="4" height="32" fill="var(--blue)"/><rect x="40" y="18" width="4" height="52" fill="var(--teal)"/><rect x="44" y="40" width="4" height="30" fill="var(--blue-soft)"/>
    <rect x="64" y="24" width="4" height="46" fill="var(--blue)"/><rect x="68" y="44" width="4" height="26" fill="var(--teal)"/><rect x="72" y="34" width="4" height="36" fill="var(--blue-soft)"/>
    <rect x="92" y="30" width="4" height="40" fill="var(--blue)"/><rect x="96" y="22" width="4" height="48" fill="var(--teal)"/><rect x="100" y="12" width="4" height="58" fill="var(--blue-soft)"/></g>
    <line x1="4" y1="70" x2="110" y2="70" stroke="#ddd" stroke-width=".5"/>
    <g font-family="Raleway" font-size="2.5" fill="#999"><text x="6" y="76">Category 1</text><text x="34" y="76">Category 2</text><text x="62" y="76">Category 3</text><text x="90" y="76">Category 4</text><text x="28" y="82">■ Series 1 ■ Series 2 ■ Series 3</text></g>
  </svg>
  <div class="foot">© Copyright 2018 Lumen Bridge Collective. All rights reserved.</div>
</section>

<!-- 16 Column chart -->
<section class="slide">
  <h2 class="title">Column Chart</h2>
  <div class="logo"><i></i>Lumen Bridge Collective</div>
  <svg class="abs" width="296" height="120" style="left:0;top:34px">
    <g font-family="Raleway" font-size="4" fill="#888">
      <rect x="28" y="16" width="11" height="90" fill="var(--blue)"/><rect x="41" y="51" width="11" height="55" fill="var(--teal)"/><rect x="54" y="69" width="11" height="37" fill="var(--blue-soft)"/>
      <text x="30" y="13">49</text><text x="43" y="48">30</text><text x="56" y="66">20</text>
      <rect x="95" y="60" width="11" height="46" fill="var(--blue)"/><rect x="108" y="26" width="11" height="80" fill="var(--teal)"/><rect x="121" y="66" width="11" height="40" fill="var(--blue-soft)"/>
      <text x="97" y="57">25</text><text x="110" y="23">44</text><text x="123" y="63">22</text>
      <rect x="162" y="40" width="11" height="66" fill="var(--blue)"/><rect x="175" y="73" width="11" height="33" fill="var(--teal)"/><rect x="188" y="28" width="11" height="78" fill="var(--blue-soft)"/>
      <text x="164" y="37">36</text><text x="177" y="70">18</text><text x="190" y="25">43</text>
      <rect x="229" y="7" width="11" height="99" fill="var(--blue)"/><rect x="242" y="55" width="11" height="51" fill="var(--teal)"/><rect x="255" y="42" width="11" height="64" fill="var(--blue-soft)"/>
      <text x="231" y="5">54</text><text x="244" y="52">28</text><text x="257" y="39">35</text>
    </g>
  </svg>
  <div class="abs" style="left:30px;top:141px;width:40px;font-size:3.5px;color:var(--teal)">Category 1<br><span class="tx">Peer circle growth.</span></div>
  <div class="abs" style="left:97px;top:141px;width:40px;font-size:3.5px;color:var(--teal)">Category 2<br><span class="tx">Event attendance.</span></div>
  <div class="abs" style="left:164px;top:141px;width:40px;font-size:3.5px;color:var(--blue-soft)">Category 3<br><span class="tx">Guides shared.</span></div>
  <div class="abs" style="left:231px;top:141px;width:40px;font-size:3.5px;color:var(--blue-soft)">Category 4<br><span class="tx">New partners.</span></div>
  <div class="foot">© Copyright 2018 Lumen Bridge Collective. All rights reserved.</div>
</section>

<!-- 17 Three Steps -->
<section class="slide">
  <h2 class="title">Three Steps</h2>
  <div class="logo"><i></i>Lumen Bridge Collective</div>
  <div class="ico" style="left:22px;top:54px"></div><div class="h6 abs" style="left:40px;top:54px">Sample Text</div><p class="tx abs" style="left:40px;top:61px;width:118px">Connect: patients join a circle of peers who understand daily life with a rare disease.</p>
  <div class="ico t" style="left:22px;top:84px"></div><div class="h6 abs" style="left:40px;top:84px;color:var(--teal)">Sample Text</div><p class="tx abs" style="left:40px;top:91px;width:118px">Learn: sessions explain treatment choices and research in clear, simple words.</p>
  <div class="ico l" style="left:22px;top:114px"></div><div class="h6 abs" style="left:40px;top:114px;color:var(--blue-soft)">Sample Text</div><p class="tx abs" style="left:40px;top:121px;width:118px">Partner: industry listens and builds awareness with the patient community.</p>
  <svg class="abs" width="110" height="140" style="left:180px;top:24px">
    <g fill="none" stroke-width="11">
      <circle cx="68" cy="36" r="20" stroke="var(--blue)"/>
      <circle cx="40" cy="75" r="20" stroke="var(--teal)"/>
      <circle cx="68" cy="112" r="20" stroke="var(--blue-soft)"/>
    </g>
    <circle cx="68" cy="36" r="12" fill="#fff"/><circle cx="40" cy="75" r="12" fill="#fff"/><circle cx="68" cy="112" r="12" fill="#fff"/>
    <g fill="none" stroke-width="1"><rect x="63" y="33" width="10" height="6" stroke="var(--blue)"/><path d="M35 79l3-4 3 2 4-5" stroke="var(--teal)"/><rect x="64" y="108" width="8" height="8" stroke="var(--blue-soft)"/></g>
  </svg>
  <div class="foot">© Copyright 2018 Lumen Bridge Collective. All rights reserved.</div>
</section>

<!-- 18 Project Timeline -->
<section class="slide">
  <h2 class="title">Project Timeline</h2>
  <div class="logo"><i></i>Lumen Bridge Collective</div>
  <svg class="abs" width="270" height="120" style="left:22px;top:38px" font-family="Raleway">
    <rect x="0" y="0" width="266" height="6" fill="#f2f2f2"/>
    <g font-size="3" fill="#777"><text x="18" y="4.5">Project step</text><text x="66" y="4.5">Jan</text><text x="82" y="4.5">Feb</text><text x="98" y="4.5">Mar</text><text x="114" y="4.5">Apr</text><text x="130" y="4.5">May</text><text x="146" y="4.5">June</text><text x="162" y="4.5">July</text><text x="178" y="4.5">Aug</text><text x="194" y="4.5">Sep</text><text x="210" y="4.5">Oct</text><text x="226" y="4.5">Nov</text><text x="242" y="4.5">Dec</text></g>
    <g stroke="#e6e6e6" stroke-width=".4"><line x1="0" y1="14.5" x2="266" y2="14.5"/><line x1="0" y1="23" x2="266" y2="23"/><line x1="0" y1="31.5" x2="266" y2="31.5"/><line x1="0" y1="40" x2="266" y2="40"/><line x1="0" y1="48.5" x2="266" y2="48.5"/><line x1="0" y1="57" x2="266" y2="57"/><line x1="0" y1="65.5" x2="266" y2="65.5"/><line x1="0" y1="74" x2="266" y2="74"/><line x1="0" y1="82.5" x2="266" y2="82.5"/><line x1="60" y1="0" x2="60" y2="84"/></g>
    <g font-size="2.8" fill="#999"><text x="20" y="12">Process 01</text><text x="20" y="20.5">Process 02</text><text x="20" y="29">Process 03</text><text x="20" y="37.5">Process 04</text><text x="20" y="46">Process 05</text><text x="20" y="54.5">Process 06</text><text x="20" y="63">Process 07</text><text x="20" y="71.5">Process 08</text><text x="20" y="80">Process 09</text></g>
    <g><rect x="66" y="9" width="30" height="3.5" rx="1.7" fill="var(--blue-mid)"/><rect x="90" y="17.5" width="58" height="3.5" rx="1.7" fill="var(--blue)"/><rect x="100" y="26" width="110" height="3.5" rx="1.7" fill="var(--teal)"/>
    <rect x="116" y="34.5" width="34" height="3.5" rx="1.7" fill="var(--blue-soft)"/><rect x="236" y="26" width="26" height="3.5" rx="1.7" fill="var(--teal)"/><rect x="156" y="43" width="96" height="3.5" rx="1.7" fill="var(--blue-soft)"/>
    <rect x="112" y="51.5" width="30" height="3.5" rx="1.7" fill="var(--teal-soft)"/><rect x="160" y="60" width="76" height="3.5" rx="1.7" fill="var(--teal)"/><rect x="200" y="68.5" width="50" height="3.5" rx="1.7" fill="var(--blue-mid)"/></g>
    <g font-size="2.8" fill="#999"><text x="30" y="97">● Description</text><text x="70" y="97">● Description</text><text x="110" y="97">● Description</text><text x="150" y="97">● Description</text><text x="190" y="97">● Description</text></g>
  </svg>
  <div class="foot">© Copyright 2018 Lumen Bridge Collective. All rights reserved.</div>
</section>

<!-- 19 Three Bullets Area -->
<section class="slide last-a">
  <h2 class="title">Three Bullets Area</h2>
  <div class="logo"><i></i>Lumen Bridge Collective</div>
  <div class="photo" role="img" aria-label="Photo of a smiling patient and caregiver" style="left:14px;top:32px;width:282px;height:72px;background:linear-gradient(90deg,#e7eef3,#c5d2db 60%,#9aaab6)"></div>
  <svg class="abs" width="296" height="40" style="left:0;top:86px">
    <circle cx="56" cy="18" r="14" fill="var(--blue)"/><circle cx="148" cy="18" r="14" fill="var(--teal)"/><circle cx="240" cy="18" r="14" fill="var(--blue-soft)"/>
    <g fill="none" stroke="#fff" stroke-width="1"><circle cx="52" cy="18" r="2"/><circle cx="60" cy="14" r="2"/><circle cx="60" cy="22" r="2"/><path d="M54 17l4-2M54 19l4 2"/>
    <path d="M142 15l6-3 6 3-6 3z M142 19l6 3 6-3 M142 22l6 3 6-3"/>
    <path d="M236 24h9 M237 24c0-4 1-6 1-8l-2-2 3-3 4 2 1 4-2 1 1 6"/></g>
  </svg>
  <p class="tx abs" style="left:30px;top:124px;width:52px;text-align:center">Peer support that helps people feel understood.</p>
  <p class="tx abs" style="left:122px;top:124px;width:52px;text-align:center">Clear resources on each treatment choice.</p>
  <p class="tx abs" style="left:214px;top:124px;width:52px;text-align:center">Strong partners who amplify the patient voice.</p>
  <div class="foot">© Copyright 2018 Lumen Bridge Collective. All rights reserved.</div>
</section>

<!-- 20 Thank You -->
<section class="slide last-b" style="background:var(--teal-mid)">
  <div class="photo" role="img" aria-label="Teal-tinted photo of a doctor with a patient" style="inset:0;background:linear-gradient(135deg,#5ec0ae,#2bae98 55%,#1e9d88)"></div>
  <div class="abs white" style="left:34px;top:50px;font-family:'Lora',serif;font-weight:600;font-size:18px">Thank You</div>
  <div class="abs white" style="left:36px;top:76px;font-size:7px">Send Your Feedback</div>
  <div class="abs" style="left:135px;top:52px;width:1px;height:56px;background:rgba(255,255,255,.6)"></div>
  <div class="abs white" style="left:140px;top:78px;font-size:14px;font-weight:300">Lumen Bridge Collective</div>
  <div class="abs tx white" style="left:36px;top:92px;line-height:2.2">
    ⌂ 24 Harbor Lane, Bridgeton<br>☎ (555) 014 2280<br>✉ hello@lumenbridge.example<br>◉ www.lumenbridge.example
  </div>
</section>

</main>
</body>
</html>
```